cartNest - a stylish trolley for apartments

We neede a simple website to sell our Trolley, for apartment use.
The colour theme is red, blask & white. Our logo is attached and this needs to be on the Home page.
The website only needs a Home Page plus 4 other pges.
In the attachment you will find a site map.

You can check out the following two sites to see what I like:
www.plinvex.example/design-showcase-inspiration/minimalist-portfolio-website/
www.brostaquill.example/inspiration/40-beautiful-web-design-portfolios/ in this site especially
Dario Pesqueta
Q L Smithy
Nine 86 Studio
Albert Crisp

And especially Lamp - I ike the simpicity of the site esp as we are only selling one product

Target Market(s)

Apartment dwellers

Industry/Entity Type

Apartment

Requirements
Must have
• This website must have 4 pages.
We need Zanto, Fundline and Quibpay portals.
Order Form for Trolley
Payment form.

```html
<!DOCTYPE html>
<html lang="en">
<head>
<meta charset="utf-8">
<title>cartNest – Home</title>
<link rel="stylesheet" href="https://fonts.googleapis.com/css2?family=PT+Sans:ital,wght@0,400;0,700;1,400&family=Arimo:wght@700&display=swap">
<style>
:root{
  --red:#e04a39;
  --red-dark:#c93b2c;
  --ink:#2b2b2b;
  --text:#3c3c3c;
  --header-bg:#f3f1f2;
  --page-bg:#ffffff;
  --panel-top:#c9c9c9;
  --panel-bottom:#f1f1f1;
  --nav-active:#7a7a7a;
  --rule:#5b5b5b;
  --white:#ffffff;
  --button:#dcdcdc;
}
*{box-sizing:border-box;margin:0;padding:0}
html,body{width:1174px;height:1200px;overflow:hidden}
body{position:relative;background:var(--page-bg);font-family:"PT Sans",sans-serif;color:var(--text)}
.abs{position:absolute}

/* header */
.top-strip{left:0;top:0;width:1174px;height:9px;background:var(--red)}
.header{left:0;top:9px;width:1174px;height:93px;background:var(--header-bg)}
.brand{left:69px;top:38px;display:flex;align-items:center;gap:8px;font-family:"PT Sans",sans-serif;font-weight:700;font-size:24px;color:var(--ink)}
.brand-mark{width:22px;height:22px;background:var(--red)}
.account-tab{left:852px;top:9px;width:203px;height:25px}
.account-links{left:880px;top:11px;width:160px;text-align:center;color:var(--white);font-size:13px;display:flex;justify-content:center;gap:12px}
.social{left:922px;top:55px;display:flex;gap:8px}
.social span{width:28px;height:30px;border-radius:4px;background:linear-gradient(#5d8ac8,#2f5fa4)}

/* navigation */
.nav{left:0;top:102px;width:1174px;height:40px;background:var(--red)}
.nav-rule{left:0;top:142px;width:1118px;height:4px;background:var(--rule)}
.nav-list{left:554px;top:102px;height:40px;display:flex;list-style:none}
.nav-list li{height:40px;line-height:40px;color:var(--white);font-size:14px;padding:0 21px}
.nav-list li.active{background:linear-gradient(#8a8a8a,#666);width:80px;padding:0;text-align:center;position:relative}
.nav-list li.active::after{content:"";position:absolute;left:36px;top:0;border:5px solid transparent;border-top-color:var(--header-bg)}

/* hero */
.hero-line{left:0;top:160px;width:1174px;height:4px;background:var(--red)}
.hero{left:0;top:164px;width:1174px;height:264px;background:linear-gradient(90deg,#8f8d6e 0%,#c9c7a6 35%,#6e6e52 60%,#b8bb8c 80%,#4f5046 100%)}
.hero-band{left:0;top:428px;width:1174px;height:24px;background:var(--red)}
.dots{left:1011px;top:433px;display:flex;gap:14px}
.dots span{width:10px;height:10px;border-radius:50%;background:var(--white)}
.dots span.current{background:#555}

/* content panels */
.panel{left:57px;width:1061px;height:254px;background:linear-gradient(var(--panel-top),var(--panel-bottom));box-shadow:0 8px 10px -8px rgba(0,0,0,.25);overflow:hidden}
.panel-welcome{top:480px}
.panel-about{top:759px}
.panel-title{display:flex;align-items:center;gap:8px;font-family:"Arimo",sans-serif;font-weight:700;font-size:15px;color:var(--ink)}
.panel-title em{font-style:normal;color:var(--red)}
.panel-rule{height:0;border-top:1px dashed #555}
.panel-copy p{font-size:13px;line-height:21px;margin-bottom:9px}
.panel-copy .tagline{font-style:italic;text-align:right;margin:-4px 0 0}
.read-more{display:flex;align-items:center;gap:6px;font-size:12.5px;color:var(--ink)}
.product-photo{border:2px solid var(--white);background:linear-gradient(#d9d6cf,#9a948a 55%,#3b3734);box-shadow:0 0 3px rgba(0,0,0,.3)}

/* footer */
.footer{left:0;top:1049px;width:1174px;height:151px;background:var(--red)}
.email-field{left:347px;top:1073px;width:265px;height:25px;background:var(--white);border-radius:4px;font-size:12px;color:#666;padding:5px 11px}
.btn{top:1073px;height:25px;border-radius:4px;background:linear-gradient(#f0f0f0,#c8c8c8);font-size:12.5px;color:var(--ink);text-align:center;line-height:25px}
.btn-subscribe{left:631px;width:96px}
.btn-unsubscribe{left:743px;width:101px}
.footer-links{left:0;top:1124px;width:1174px;display:flex;justify-content:center;list-style:none;color:var(--white);font-size:14px;padding-left:8px}
.footer-links li+li::before{content:"|";margin:0 19px}
.copyright{left:0;top:1160px;width:1174px;text-align:center;color:var(--white);font-size:12px}
.copyright b{font-weight:400;color:var(--ink)}
.page-code{left:1126px;top:1160px;color:var(--white);font-size:12.5px}
</style>
</head>
<body>

<div class="abs header"></div>
<div class="abs top-strip"></div>

<div class="abs brand"><span class="brand-mark"></span>cartNest</div>

<svg class="abs account-tab" viewBox="0 0 203 25" aria-hidden="true"><path d="M0 0H203L191 25H12Z" fill="#e04a39"/></svg>
<div class="abs account-links"><span>Register</span><span>/</span><span>Signin</span></div>

<div class="abs social" aria-label="Social links"><span></span><span></span><span></span></div>

<div class="abs nav"></div>
<ul class="abs nav-list">
  <li class="active">Home</li>
  <li>My trolley</li>
  <li>Gallery</li>
  <li>Contact us</li>
  <li>Shopping cart paymeny</li>
</ul>
<div class="abs nav-rule"></div>

<div class="abs hero-line"></div>
<div class="abs hero" role="img" aria-label="Photo: a couple handing luggage from a car boot onto a trolley in a parking garage"></div>
<div class="abs hero-band"></div>
<div class="abs dots"><span></span><span class="current"></span><span></span><span></span></div>

<section class="abs panel panel-welcome">
  <h2 class="abs panel-title" style="left:18px;top:10px">
    <svg width="16" height="16" viewBox="0 0 16 16" aria-hidden="true"><circle cx="8" cy="8" r="7" fill="none" stroke="#2b2b2b" stroke-width="1.3"/><path d="M9.5 4.5L6 8l3.5 3.5" fill="none" stroke="#2b2b2b" stroke-width="1.5"/></svg>
    <span>cart<em>Nest</em>&nbsp; <em>Welcomes you</em></span>
  </h2>
  <div class="abs panel-rule" style="left:18px;top:39px;width:874px"></div>
  <div class="abs panel-copy" style="left:18px;top:50px;width:874px">
    <p>cartNest evolved from demand! &nbsp;Apartment dwellers everywhere are calling for a solution to moving shopping, luggage and other goods from car to apartment, and vice versa. Other trolleys on the market are not versatile, they are not robust, but more importantly, they are NOT stylish! The emphasis of cartNest is on style. This trolley is stylish enough to remain in your apartment as a piece of furniture. It features a versatile flat-bed and hanger, to cope with all your transport needs.</p>
    <p>cartNest is made of high quality stainless steel and other robust materials. Whilst other trolleys tend to look like they belong in a factory or workshop, cartNest is the classy alternative, which can live anywhere in your apartment, and not in the cupboard.</p>
    <p class="tagline">So – we welcome cartNest to the marketplace!</p>
  </div>
  <div class="abs read-more" style="left:802px;top:224px">Read more
    <svg width="15" height="15" viewBox="0 0 16 16" aria-hidden="true"><circle cx="8" cy="8" r="7" fill="none" stroke="#555" stroke-width="1.2"/><path d="M6.5 4.5L10 8l-3.5 3.5" fill="none" stroke="#555" stroke-width="1.4"/></svg>
  </div>
  <div class="abs product-photo" style="left:912px;top:42px;width:136px;height:199px" role="img" aria-label="Photo: the chrome trolley loaded with red suitcases and garments"></div>
</section>

<section class="abs panel panel-about">
  <div class="abs product-photo" style="left:12px;top:41px;width:136px;height:201px" role="img" aria-label="Photo: the chrome trolley with hanging clothes and red luggage"></div>
  <h2 class="abs panel-title" style="left:163px;top:12px">
    <svg width="16" height="16" viewBox="0 0 16 16" aria-hidden="true"><circle cx="8" cy="8" r="7" fill="none" stroke="#2b2b2b" stroke-width="1.3"/><path d="M9.5 4.5L6 8l3.5 3.5" fill="none" stroke="#2b2b2b" stroke-width="1.5"/></svg>
    <span>About <em>us</em></span>
  </h2>
  <div class="abs panel-rule" style="left:163px;top:39px;width:875px"></div>
  <div class="abs panel-copy" style="left:162px;top:50px;width:878px">
    <p>Lorem Ipsum is simply dummy text of the printing and typesetting industry. Lorem Ipsum has been the industry's standard dummy text ever since the 1500s, when an unknown printer took a galley of type and scrambled it to make a type specimen book. It has survived not only five centuries, but also the leap into electronic typesetting, remaining essentially unchanged.</p>
    <p>&nbsp;It was popularised in the 1960s with the release of Lettrafix sheets containing Lorem Ipsum passages, and more recently with desktop publishing software like Orvel PageSetter including versions of Lorem Ipsum.</p>
    <p class="tagline" style="margin-top:4px">Lorem Ipsum is simply dummy text of the printing and typesetting industry.</p>
  </div>
  <div class="abs read-more" style="left:948px;top:224px">Read more
    <svg width="15" height="15" viewBox="0 0 16 16" aria-hidden="true"><circle cx="8" cy="8" r="7" fill="none" stroke="#555" stroke-width="1.2"/><path d="M6.5 4.5L10 8l-3.5 3.5" fill="none" stroke="#555" stroke-width="1.4"/></svg>
  </div>
</section>

<footer>
  <div class="abs footer"></div>
  <div class="abs email-field">Enter the email address...</div>
  <div class="abs btn btn-subscribe">Subscribe</div>
  <div class="abs btn btn-unsubscribe">Unsubscribe</div>
  <ul class="abs footer-links">
    <li>Home</li><li>My trolley</li><li>Gallery</li><li>Contact us</li><li>Shopping cart paymeny</li><li>Privacy policy</li><li>Terms &amp; Conditions</li><li>Help</li>
  </ul>
  <div class="abs copyright">© 2012 &nbsp;copyrights <b>cart</b>nest.example. All rights reserved.</div>
  <div class="abs page-code">X40</div>
</footer>

</body>
</html>
```